8 New Banner Campaigns

Task Description
I want banners created for 8 campaigns.

For each campaign I need these 6 banner sizes created:

Web Banner Sizes (300x250, 468x60, 160x600)
One of each of these sizes, so 3 web banners

Mobile Banner Sizes (300x50, 216x36, 240x240)

campaign 1
http://brivapagehost.com/_PROJECT_/fundmarket/index.php
Done right
$10,000 Money-back guarantee!

Call Now For Your Top Local Electrician!

campaign2
http://www.palmcrestretreat.com

a weight loss journey that can change your life

campaign 3
http://www.norvexlistings.com/m/delta-in-financial-planner/

Professional financial planning
Tax planning
Estate planning
Retirement planning
Wealth Management

Call Now for Details!

campaign4
www.areatradeappraisals.com/Farmington-CT/KIVO-Insurance-Agency-81342.html

Business insurance free quotes

campaign5
Summit debtrelief
http://www.norvexlistings.com/m/dayton-oh-bankruptcy-attorney/

Call Now for a No Cost Evaluation by a participating Summit Debtrelief Attorney.

campaign 6
http://brivapagehost.com/_PROJECT_/harbors/index.php

Is a reverse mortgage right for you?

Cash to live on while you stay in your home

Our caring experts will explain your options-Call Now

In tiny text at bottom:
No reverse mortgages in MD, IL, RI, and NC

campaign 7
http://www.freewheel-legal.com/

Dransfeld Law DUI defense

Campaign 8
http://www.craftacademies.edu/

The Craft Academies

Need these done ASAP..more to come!

Industry/Entity Type

Financial

Requirements
Must have
• Phone Number call to action on all banners.

```html
<!DOCTYPE html>
<html lang="en">
<head>
<meta charset="utf-8">
<title>Campaign 1 – Electrician Banner</title>
<link rel="stylesheet" href="https://fonts.googleapis.com/css2?family=Questrial&family=Poppins:wght@600;700&display=swap">
<style>
  :root {
    --slide-grey: #8f959d;
    --slide-grey-light: #a2a8b0;
    --label-black: #0d0d0d;
    --frame-white: #ffffff;
    --sky-deep: #2394cc;
    --sky-light: #6fc2e8;
    --ink: #1a1a1a;
    --paper: #ffffff;
    --figure-skin: #e9b89a;
    --figure-hair: #8a5a34;
  }
  * { box-sizing: border-box; margin: 0; padding: 0; }
  html, body {
    width: 1200px; height: 900px; overflow: hidden;
  }
  body {
    position: relative;
    background: radial-gradient(ellipse at 55% 40%, var(--slide-grey-light), var(--slide-grey) 75%);
    font-family: "Poppins", sans-serif;
  }
  .slide-label {
    position: absolute; left: 0; top: 30px;
    width: 1000px; height: 63px;
    background: linear-gradient(90deg, var(--label-black) 0%, rgba(13,13,13,0.75) 20%, rgba(13,13,13,0) 90%);
    color: #fff;
    font-family: "Questrial", sans-serif;
    font-size: 34px;
    line-height: 63px;
    padding-left: 44px;
    letter-spacing: 0.5px;
  }
  .banner {
    position: absolute; left: 300px; top: 200px;
    width: 600px; height: 500px;
    background: var(--frame-white);
    padding: 7px;
  }
  .banner-reflection {
    position: absolute; left: 300px; top: 700px;
    width: 600px; height: 110px;
    background: linear-gradient(180deg, rgba(255,255,255,0.12), rgba(255,255,255,0));
  }
  .banner-field {
    position: relative; width: 100%; height: 100%; overflow: hidden;
    background:
      radial-gradient(ellipse at 45% 100%, var(--sky-light) 0%, rgba(111,194,232,0.4) 45%, rgba(111,194,232,0) 75%),
      linear-gradient(160deg, var(--sky-deep) 0%, #3aa6d9 50%, var(--sky-deep) 100%);
  }
  .outlined {
    position: absolute;
    color: var(--paper);
    font-weight: 700;
    white-space: nowrap;
    text-align: center;
    text-shadow:
      2px 0 0 var(--ink), -2px 0 0 var(--ink), 0 2px 0 var(--ink), 0 -2px 0 var(--ink),
      1.5px 1.5px 0 var(--ink), -1.5px -1.5px 0 var(--ink), 1.5px -1.5px 0 var(--ink), -1.5px 1.5px 0 var(--ink);
  }
  .headline { left: 0; width: 586px; top: 22px; font-size: 62px; line-height: 80px; }
  .call-line { left: 0; width: 586px; top: 124px; font-size: 23px; line-height: 34px; letter-spacing: -0.3px; }
  .phone { left: 0; width: 586px; top: 168px; font-size: 76px; line-height: 94px; letter-spacing: -1px; }
  .amount { left: 232px; width: 346px; top: 322px; font-size: 82px; line-height: 100px; letter-spacing: -1px; }
  .guarantee { left: 232px; width: 346px; top: 430px; font-size: 23px; line-height: 34px; letter-spacing: -0.3px; }
  .operator-figure {
    position: absolute; left: 0; top: 308px;
    width: 178px; height: 178px;
    background: linear-gradient(135deg, var(--figure-hair) 0%, var(--figure-skin) 45%, #8fc9e8 100%);
    border-top-right-radius: 40px;
  }
  .speech-bubble {
    position: absolute; left: 78px; top: 340px;
    width: 152px; height: 74px;
  }
  .speech-bubble svg { position: absolute; inset: 0; }
  .speech-text {
    position: absolute; inset: 0;
    display: flex; flex-direction: column; align-items: center; justify-content: center;
    color: var(--ink); font-weight: 600; text-align: center;
    padding-left: 10px;
  }
  .speech-text .small { font-size: 10px; line-height: 13px; }
  .speech-text .big { font-size: 15px; line-height: 19px; font-weight: 700; }
</style>
</head>
<body>
  <div class="slide-label">campaign 1</div>

  <div class="banner-reflection"></div>
  <div class="banner">
    <div class="banner-field">
      <div class="outlined headline">Done Right!</div>
      <div class="outlined call-line">Call Now For Your Top Local Electrician!</div>
      <div class="outlined phone">555-555-5555</div>

      <div class="operator-figure" role="img" aria-label="Retro illustration of a call-centre operator with headset holding a phone"></div>
      <div class="speech-bubble">
        <svg viewBox="0 0 152 74" width="152" height="74">
          <path d="M20 34 L2 40 L18 44 Z" fill="#fff" stroke="#1a1a1a" stroke-width="1.5"/>
          <ellipse cx="82" cy="37" rx="68" ry="34" fill="#fff" stroke="#1a1a1a" stroke-width="1.5"/>
        </svg>
        <div class="speech-text">
          <span class="small">Get your honey-do list</span>
          <span class="big">DONE RIGHT!</span>
        </div>
      </div>

      <div class="outlined amount">$10,000</div>
      <div class="outlined guarantee">Money-Back Guarantee!</div>
    </div>
  </div>
</body>
</html>
```